Laundry pickup and delivery flyer "Suds Harbor laundry"

I need a flyer "8.5"x11" that tells customers about our pickup and delivery laundry service. our website address is: www.sudsharborlaundry.example The flyer should be front and back.

Font styles to use
Sans Serif

Colors
0094D4
00A9DD
6FCCEA
C7EBF8
E9F6FB

```html
<!DOCTYPE html>
<html lang="en">
<head>
<meta charset="utf-8">
<title>Suds Harbor Laundry – Pickup &amp; Delivery Flyer</title>
<link href="https://fonts.googleapis.com/css2?family=Barlow:wght@400;500;600;700&family=Barlow+Condensed:wght@600;700&family=Montserrat:wght@800&display=swap" rel="stylesheet">
<style>
  :root{
    --backdrop:#858585;
    --royal:#0a57d0;
    --royal-deep:#0548c0;
    --brand-blue:#0094D4;
    --sky:#00A9DD;
    --light:#6FCCEA;
    --pale:#C7EBF8;
    --mist:#E9F6FB;
    --cyan-title:#12eef8;
    --headline-blue:#1a4fd4;
    --step-line:#4a8cf0;
    --ink:#000;
    --white:#fff;
  }
  *{box-sizing:border-box;margin:0;padding:0}
  html,body{width:1200px;height:1200px;overflow:hidden;background:var(--backdrop)}
  body{position:relative;font-family:"Barlow",sans-serif}
  .flyer{position:absolute;left:180px;top:56px;width:840px;height:1088px;background:var(--white);overflow:hidden}
  .laundromat-photo{position:absolute;left:180px;top:0;width:660px;height:300px;
    background:linear-gradient(90deg,rgba(255,255,255,1) 0%,rgba(205,208,210,.6) 35%,#9ea3a6 70%,#7d8286 100%)}
  .header-wave,.foam-band{position:absolute;left:0;width:840px}
  .header-wave{top:150px;height:600px}
  .brand-mark{position:absolute;left:84px;top:106px;display:flex;align-items:center;gap:12px}
  .brand-dot{width:36px;height:36px;border-radius:50%;background:var(--brand-blue)}
  .brand-name{font-family:"Barlow",sans-serif;font-weight:700;font-size:44px;color:var(--brand-blue);line-height:1}
  .bags-photo{position:absolute;left:523px;top:92px;width:208px;height:208px;border-radius:50%;border:6px solid var(--white);
    background:radial-gradient(circle at 50% 45%,#25407a 0%,#1c2f5c 55%,#6b4a2e 100%)}
  .title{position:absolute;left:0;width:840px;top:320px;text-align:center;font-family:"Montserrat",sans-serif;font-weight:800;font-size:84px;letter-spacing:2px;color:var(--cyan-title);line-height:1}
  .tagline{position:absolute;left:0;width:840px;top:418px;text-align:center;font-weight:600;font-size:40px;line-height:1;color:var(--white)}
  .steps{position:absolute;left:0;top:475px;width:840px;height:210px}
  .step-icons{position:absolute;left:0;top:0}
  .step-box{position:absolute;top:77px;width:172px;height:127px;border:2px solid var(--step-line);border-radius:12px;
    padding:30px 6px 0;text-align:center;color:var(--white);font-size:15.5px;line-height:21px;font-weight:500}
  .web{position:absolute;left:0;width:840px;top:696px;text-align:center;font-weight:600;font-size:29px;line-height:36px;color:var(--white);display:flex;justify-content:center;align-items:center;gap:10px}
  .foam-band{top:733px;height:310px;background:linear-gradient(180deg,rgba(111,204,234,0) 0%,var(--pale) 25%,var(--mist) 60%,var(--white) 100%);border-radius:60px 60px 0 0}
  .van-photo{position:absolute;left:65px;top:857px;width:420px;height:155px;border-radius:18px 40px 14px 14px;
    background:linear-gradient(90deg,#2f74c8 0%,#4f9de0 30%,#f4f8fb 45%,#ffffff 70%,#3d86d6 100%)}
  .headline{position:absolute;left:550px;top:862px;font-family:"Barlow Condensed",sans-serif;font-weight:700;font-size:62px;line-height:67px;color:var(--headline-blue)}
  .footer-bar{position:absolute;left:0;top:1020px;width:840px;height:68px}
  .schedule{position:absolute;left:0;top:1041px;width:400px;text-align:center;font-family:"Barlow Condensed",sans-serif;font-weight:700;font-size:34px;line-height:40px;color:var(--white)}
  .call{position:absolute;left:400px;top:1034px;width:440px;text-align:center;font-weight:600;font-size:36px;line-height:44px;color:var(--white)}
</style>
</head>
<body>
<main class="flyer">
  <div class="laundromat-photo" role="img" aria-label="Photo of a row of stainless steel front-load washers in the laundromat"></div>

  <svg class="header-wave" viewBox="0 150 840 600" aria-hidden="true">
    <path d="M0 206 C220 300 520 310 840 210 L840 740 L0 740 Z" fill="var(--royal)"/>
    <path d="M0 206 C220 300 520 310 840 210 L840 245 C560 335 240 325 0 222 Z" fill="var(--white)"/>
    <path d="M560 300 C680 280 760 250 840 235 L840 345 C760 300 680 290 560 300 Z" fill="var(--sky)" opacity=".8"/>
    <path d="M640 170 L840 105 L840 210 C760 230 700 250 640 265 Z" fill="var(--royal-deep)"/>
  </svg>

  <div class="brand-mark"><span class="brand-dot"></span><span class="brand-name">Suds Harbor</span></div>

  <div class="bags-photo" role="img" aria-label="Photo of two branded laundry bags left on a welcome mat"></div>

  <h1 class="title">SUDS HARBOR</h1>
  <p class="tagline">Jackson’s Premier Laundry Service</p>

  <section class="steps">
    <svg class="step-icons" width="840" height="100" viewBox="0 0 840 100" aria-hidden="true">
      <line x1="0" y1="47" x2="840" y2="47" stroke="var(--step-line)" stroke-width="3"/>
      <g fill="var(--step-line)" stroke="var(--royal)" stroke-width="2">
        <circle cx="254" cy="47" r="9"/><circle cx="430" cy="47" r="9"/><circle cx="627" cy="47" r="9"/>
      </g>
      <g fill="none" stroke="var(--royal)" stroke-width="2.5"><path d="M251 42 l5 5 -5 5"/><path d="M427 42 l5 5 -5 5"/><path d="M624 42 l5 5 -5 5"/></g>
      <g fill="var(--light)" stroke="var(--step-line)" stroke-width="5">
        <circle cx="166" cy="47" r="44"/><circle cx="350" cy="47" r="44"/><circle cx="535" cy="47" r="44"/><circle cx="720" cy="47" r="44"/>
      </g>
      <circle cx="166" cy="47" r="26" fill="none" stroke="var(--white)" stroke-width="3"/>
      <path d="M166 31 V47 L178 41" fill="none" stroke="var(--white)" stroke-width="3" stroke-linecap="round"/>
      <path d="M320 60 V40 L330 28 H378 V60 Z" fill="none" stroke="var(--white)" stroke-width="3" stroke-linejoin="round"/>
      <circle cx="333" cy="61" r="6" fill="var(--light)" stroke="var(--white)" stroke-width="3"/>
      <circle cx="366" cy="61" r="6" fill="var(--light)" stroke="var(--white)" stroke-width="3"/>
      <line x1="318" y1="72" x2="380" y2="72" stroke="var(--white)" stroke-width="2"/>
      <rect x="514" y="22" width="42" height="50" rx="4" fill="var(--white)"/>
      <circle cx="535" cy="52" r="14" fill="var(--light)"/>
      <path d="M521 53 q7 -5 14 0 t14 0 v1 a14 14 0 0 1 -28 0 z" fill="var(--brand-blue)"/>
      <circle cx="520" cy="29" r="2" fill="var(--light)"/><circle cx="526" cy="29" r="2" fill="var(--light)"/>
      <path d="M716 24 a5 5 0 1 1 5 5 v6 L696 50 H744 L721 35" fill="none" stroke="var(--white)" stroke-width="3" stroke-linejoin="round"/>
      <rect x="703" y="50" width="34" height="22" fill="var(--white)"/>
    </svg>
    <p class="step-box" style="left:80px">Schedule a pickup here feel free to leave your bag where our driver can get to it.</p>
    <p class="step-box" style="left:265px">Our driver will pickup your clothes at the scheduled time.</p>
    <p class="step-box" style="left:450px">Your clothes are expertly cleaned by our team of laundry professionals</p>
    <p class="step-box" style="left:634px">We delivery your clean clothes back to you at your convenience!</p>
  </section>

  <p class="web">
    <svg width="18" height="18" viewBox="0 0 18 18" aria-hidden="true"><g fill="none" stroke="var(--white)" stroke-width="1.6"><circle cx="9" cy="9" r="7.5"/><ellipse cx="9" cy="9" rx="3.2" ry="7.5"/><line x1="1.5" y1="9" x2="16.5" y2="9"/></g></svg>
    www.sudsharborlaundry.example
  </p>

  <div class="foam-band" role="img" aria-label="Soft soap foam and bubbles rising along the bottom of the flyer"></div>

  <div class="van-photo" role="img" aria-label="Photo of the branded pickup and delivery van"></div>

  <h2 class="headline">Free Pickup<br>&amp; Delivery</h2>

  <svg class="footer-bar" viewBox="0 0 840 68" aria-hidden="true">
    <rect x="0" y="15" width="420" height="53" fill="var(--ink)"/>
    <polygon points="403,0 840,0 840,68 384,68" fill="var(--royal)"/>
    <polygon points="403,0 840,0 840,24 398,24" fill="var(--sky)"/>
  </svg>
  <p class="schedule">SCHEDULE PICKUP</p>
  <p class="call">Call us at 555-014-0392</p>
</main>
</body>
</html>
```